Professional business cards for real estate development company

I need business cards for my new real estate development company. The company, "KORVA" is a real estate development, investment, and advisory firm with a focus on multifamily, office, and mixed-use projects across primary and secondary markets in the Southeast United States.

Style preference is modern

Industry/Entity Type

Real Estate Development

Contact Information for Business Card

The business cards need to include:
Name
Title
Mailing Address
Phone Number
Web Address

Logo is attached. I would like white to be the primary color with incorporation of the company colors: #232D3A and #B5A451

Font styles to use
Other font styles liked:
• Montserrat, Avenir

Requirements
Must have
• Company Logo. No need to include the company name since the name is in the logo.
Should not have
• No line type designs

```html
<!DOCTYPE html>
<html lang="en">
<head>
<meta charset="UTF-8">
<title>KORVA Business Card</title>
<link href="https://fonts.googleapis.com/css2?family=Lato:wght@300;400;700&display=swap" rel="stylesheet">
<style>
  :root {
    --page-bg: #e9e6e1;
    --card-gold: #b5a451;
    --card-navy: #232d3a;
    --seal-cream: #efe9dc;
    --ink-dark: #2a3340;
    --ink-light: #f4efe2;
  }
  * { margin: 0; padding: 0; box-sizing: border-box; }
  html, body {
    width: 1200px;
    height: 1047px;
    overflow: hidden;
    background: var(--page-bg);
    font-family: "Lato", sans-serif;
  }
  .card {
    position: absolute;
    left: 100px;
    top: 253px;
    width: 1000px;
    height: 540px;
    border-radius: 22px;
    overflow: hidden;
    background: var(--card-gold);
    box-shadow: 0 12px 40px rgba(35, 45, 58, 0.18);
  }
  .card__band {
    position: absolute;
    top: 0;
    right: 0;
    width: 273px;
    height: 100%;
    background: var(--card-navy);
  }
  .card__seal {
    position: absolute;
    left: 502px;
    top: 52px;
    width: 440px;
    height: 440px;
    border-radius: 50%;
    background: var(--seal-cream);
    display: flex;
    align-items: center;
    justify-content: center;
    gap: 14px;
  }
  .seal__mark {
    width: 22px;
    height: 22px;
    background: var(--card-navy);
  }
  .seal__name {
    font-weight: 700;
    font-size: 64px;
    letter-spacing: 4px;
    color: var(--card-navy);
  }
  .holder {
    position: absolute;
    left: 69px;
    top: 88px;
  }
  .holder__name {
    font-weight: 700;
    font-size: 40px;
    letter-spacing: 1px;
    color: var(--ink-dark);
    line-height: 1;
  }
  .holder__title {
    margin-top: 12px;
    font-weight: 400;
    font-size: 25px;
    color: var(--ink-light);
  }
  .divider {
    position: absolute;
    left: 69px;
    top: 246px;
    width: 56px;
    height: 2px;
    background: var(--ink-dark);
  }
  .address {
    position: absolute;
    left: 64px;
    top: 286px;
    font-size: 24px;
    line-height: 33px;
    color: var(--ink-light);
  }
  .contacts {
    position: absolute;
    left: 64px;
    top: 369px;
    list-style: none;
  }
  .contacts__item {
    display: flex;
    align-items: center;
    height: 37px;
    font-size: 24px;
    color: var(--ink-light);
  }
  .contacts__icon {
    width: 24px;
    height: 24px;
    margin-right: 25px;
    flex: none;
  }
</style>
</head>
<body>
  <div class="card">
    <div class="card__band"></div>
    <div class="card__seal">
      <span class="seal__mark"></span>
      <span class="seal__name">KORVA</span>
    </div>

    <div class="holder">
      <div class="holder__name">JOHN SMITH</div>
      <div class="holder__title">Founder &amp; CEO</div>
    </div>
    <div class="divider"></div>

    <div class="address">
      1234 First Line Address<br>
      5678 Second Line Address
    </div>

    <ul class="contacts">
      <li class="contacts__item">
        <svg class="contacts__icon" viewBox="0 0 24 24" aria-hidden="true">
          <path d="M6.6 10.8a15.2 15.2 0 0 0 6.6 6.6l2.2-2.2a1 1 0 0 1 1-.25 11.4 11.4 0 0 0 3.6.57 1 1 0 0 1 1 1V20a1 1 0 0 1-1 1A17 17 0 0 1 3 4a1 1 0 0 1 1-1h3.5a1 1 0 0 1 1 1c0 1.25.2 2.45.57 3.57a1 1 0 0 1-.25 1z" fill="#2a3340"/>
        </svg>
        1234567890
      </li>
      <li class="contacts__item">
        <svg class="contacts__icon" viewBox="0 0 24 24" aria-hidden="true">
          <rect x="2" y="5" width="20" height="14" fill="#2a3340"/>
          <path d="M2.5 5.5 12 13l9.5-7.5" fill="none" stroke="#b5a451" stroke-width="1.6"/>
        </svg>
        info@yourmail.com
      </li>
      <li class="contacts__item">
        <svg class="contacts__icon" viewBox="0 0 24 24" aria-hidden="true">
          <circle cx="12" cy="12" r="10" fill="#2a3340"/>
          <g fill="none" stroke="#b5a451" stroke-width="1.2">
            <ellipse cx="12" cy="12" rx="4" ry="10"/>
            <path d="M2 12h20M4 7h16M4 17h16"/>
          </g>
        </svg>
        www.yourwebsite.com
      </li>
    </ul>
  </div>
</body>
</html>
```